Brightford Lingua Partners, LLC

We need a business card that includes information about our business and conveys a reliable business that provides document translation services and interpreters for a variety of corporate and individual clients. We want to come across as professional, reliable, yet approachable. It should include the following on one side:

ESL / ENL Language Classes, Private Lessons, and Online Tutors
PALQE Training and Testing
Translating & Interpreting Services
Contact us about Over-the-Phone Interpreting in over 200 languages
24/7/365
www.brightfordlingua.example

The other side should include (555) 481-3062

Marla Quennick, President
412 Garvin Ave., Ste. 209
Indianapolis, IN 46999
Updates

Please add USA as part of the address. Also, please add mrqquennick@brightfordlinguapartners.example as the e-mail address. Thank you.

Target Market(s)

Business professionals, their families, the international community

Industry/Entity Type

Business

Contact Information for Business Card

24/7/365
www.brightfordlingua.example

(555) 481-3062

Marla Quennick, President
412 Garvin Ave., Ste. 209
Indianapolis, IN 46999
USA

Font styles to use
Sans Serif

Colors

Designer to choose colors to be used in the design.

Requirements
Must have
• See project description
• e-mail address and web address
• Phone number
Nice to have
• a globe
• physical address
Should not have
• Should not have the same color scheme as other agencies in our market in Indiana unless it is blue and black. No purple or yellow.

```html
<!DOCTYPE html>
<html lang="en">
<head>
<meta charset="utf-8">
<title>Brightford Lingua Partners – Business Card</title>
<link rel="stylesheet" href="https://fonts.googleapis.com/css2?family=Montserrat:wght@400;500;600;700&display=swap">
<style>
  :root {
    --page-bg: #e9ebee;
    --card-white: #ffffff;
    --brand-blue: #1e8fd0;
    --brand-blue-light: #5db8ea;
    --ink: #1a1a1a;
    --globe-tint: #eceef0;
  }
  * { box-sizing: border-box; margin: 0; padding: 0; }
  html, body { width: 1200px; height: 900px; overflow: hidden; }
  body {
    background: var(--page-bg);
    font-family: "Montserrat", Arial, sans-serif;
    color: var(--ink);
    position: relative;
  }
  .card {
    position: absolute;
    left: 250px;
    width: 700px;
    height: 400px;
    border-radius: 26px;
    background: var(--card-white);
    overflow: hidden;
    box-shadow: 0 6px 18px rgba(0,0,0,0.12);
  }
  .card--front { top: 35px; }
  .card--back { top: 465px; }

  /* brand lockup */
  .brand { position: absolute; display: flex; align-items: center; gap: 14px; }
  .brand__dot {
    width: 92px; height: 92px; border-radius: 50%;
    background: var(--brand-blue); flex: none;
  }
  .brand__name {
    font-weight: 500; font-size: 30px; line-height: 1.05; color: var(--ink);
  }

  /* front */
  .card--front .brand { left: 40px; top: 62px; }
  .services {
    position: absolute; left: 400px; top: 34px; width: 280px;
    list-style: none; color: var(--brand-blue);
    font-weight: 600; font-size: 17px; line-height: 1.2;
  }
  .services li { padding-left: 12px; position: relative; }
  .services li::before { content: "•"; position: absolute; left: 0; }
  .band {
    position: absolute; left: 0; right: 0; bottom: 0; height: 200px;
    background: var(--brand-blue);
    text-align: center; color: var(--card-white);
    padding-top: 24px;
  }
  .band__headline {
    font-weight: 600; font-size: 29px; letter-spacing: 1.5px;
    line-height: 1.2; text-transform: uppercase;
  }
  .band__hours {
    font-weight: 500; font-size: 38px; color: var(--brand-blue-light);
    margin-top: 10px;
  }
  .band__web { font-weight: 500; font-size: 20px; margin-top: 6px; }

  /* back */
  .globe-area {
    position: absolute; left: 250px; top: 10px; width: 380px; height: 380px;
    border-radius: 50%; background: var(--globe-tint);
  }
  .card--back .brand { left: 52px; top: 140px; }
  .divider {
    position: absolute; left: 398px; top: 88px; width: 2px; height: 200px;
    background: var(--brand-blue);
  }
  .contact { position: absolute; left: 432px; top: 100px; }
  .contact__name, .contact__title {
    color: var(--brand-blue); font-weight: 700; font-size: 19px;
    text-transform: uppercase; line-height: 1.15;
  }
  .contact__phone { font-weight: 500; font-size: 19px; margin-top: 16px; }
  .contact__address { font-weight: 500; font-size: 19px; line-height: 1.25; margin-top: 14px; }
  .contact__email {
    position: absolute; left: 0; right: 0; bottom: 34px;
    text-align: center; font-weight: 500; font-size: 18px; color: var(--brand-blue);
  }
</style>
</head>
<body>
  <section class="card card--front" aria-label="Card front">
    <div class="brand">
      <span class="brand__dot"></span>
      <span class="brand__name">Brightford<br>Lingua<br>Partners LLC</span>
    </div>
    <ul class="services">
      <li>ESL / ENL Language Classes, Private Lessons and Online Tutors</li>
      <li>PALQE Training and Testing</li>
      <li>Translating &amp; Interpreting Services</li>
    </ul>
    <div class="band">
      <p class="band__headline">Contact us about over-the-phone<br>interpreting in over 200 languages</p>
      <p class="band__hours">24/7/365</p>
      <p class="band__web">www.brightfordlingua.example</p>
    </div>
  </section>

  <section class="card card--back" aria-label="Card back">
    <div class="globe-area" role="img" aria-label="Faint globe illustration in the background"></div>
    <div class="brand">
      <span class="brand__dot"></span>
      <span class="brand__name">Brightford<br>Lingua<br>Partners LLC</span>
    </div>
    <div class="divider"></div>
    <div class="contact">
      <p class="contact__name">Marla Quennick</p>
      <p class="contact__title">President</p>
      <p class="contact__phone">(555) 481-3062</p>
      <p class="contact__address">412 Garvin Ave., Ste. 209<br>Indianapolis, IN 46999<br>USA</p>
    </div>
    <p class="contact__email">mrqquennick@brightfordlinguapartners.example</p>
  </section>
</body>
</html>
```